Innovative Australian Importation company in Sustainability space needs beautiful website*

We seek your services to provide a clean, modern we rendered logo for or company Red Fern Coastal Supply Pty Ltd, this will be used in all the usual places however you will aso build us our business cards and our website: redferncoastalsupply.example

What we do:
We source innovative products that solve problems in the Aeroponics, Hydroponics, Horticultural, Organics and sustainability space. We source our product from all over the world however our cliant base is predominantly in Australia & New Zealand Region.
Our company's mission is to help retail businesses by providing high-quality products at a competitive price for everyday people to produce healthy sustainable consumables from home, making it easy for the end-user to become more self-sufficient with while remaining environmentally friendly.

Target Market(s)

Aeroponics, Hydroponics, Horticultural, Organics and sustainability space.

Industry/Entity Type

Wholesale

Contact Information for Business Card

We would like these to be very modern and glossy possibly an embosed logo or rounded edges, a little smaller than the traditional?

Logo Text

Red Fern Coastal Supply

Coding

Coded - Design and coding required

Number of Pages Required

1 page

Colors
0355a3

Requirements
Must have
• The websit is bit of a landing page that will provide some minor information on our imported products. and qualify resellers ( Our target Market) from retail clients (the end-user) and provide a private store and check out for our trade customers. (not for Reatil)
Abillity to set up a trade account (must have our approval befor being granted access to shop.)
the abillity to for OEM's and International wholsalers register intrest.
The abillity to register/inquire about our produtc lines for Retailer.
The abillity to provide the end-user a list of resellers.
The ability for promo video
Nice to have
• .
Should not have
• Logo high gloss, 3d rendered

```html
<!DOCTYPE html>
<html lang="en">
<head>
<meta charset="utf-8">
<title>Red Fern Coastal Supply – Business Card</title>
<link rel="stylesheet" href="https://fonts.googleapis.com/css2?family=Roboto:wght@400;500&display=swap">
<style>
  :root {
    --ink: #000000;
    --paper: #ffffff;
    --sky: #1b93c4;
    --leaf: #2ecc71;
    --teal: #2aa3d3;
    --stage-top: #e9e9e9;
    --stage-bottom: #ffffff;
  }
  * { margin: 0; padding: 0; box-sizing: border-box; }
  html, body { width: 1016px; height: 1200px; overflow: hidden; }
  body {
    position: relative;
    font-family: "Roboto", Arial, sans-serif;
    background: linear-gradient(180deg, var(--stage-top) 0%, var(--stage-bottom) 45%);
  }
  .card {
    position: absolute;
    left: 92px;
    width: 826px;
    height: 467px;
    background: var(--ink);
    border-radius: 0 64px 0 64px;
    overflow: hidden;
    color: var(--paper);
  }
  .card--front { top: 97px; }
  .card--back { top: 628px; }
  .card__waves { position: absolute; left: 0; top: 0; width: 826px; height: 467px; }
  .wave--sky { fill: var(--sky); }
  .wave--leaf { fill: var(--leaf); }

  .brand { position: absolute; display: flex; align-items: center; }
  .brand__dot { border-radius: 50%; background: var(--teal); flex: none; }
  .brand__name {
    color: var(--teal);
    font-weight: 500;
    text-transform: uppercase;
    letter-spacing: 0.08em;
    line-height: 1.15;
  }
  .card--front .brand {
    left: 40px; top: 88px; width: 300px;
    flex-direction: column; text-align: center;
  }
  .card--front .brand__dot { width: 110px; height: 110px; margin-bottom: 24px; }
  .card--front .brand__name { font-size: 24px; }

  .card--back .brand { left: 150px; top: 130px; gap: 34px; }
  .card--back .brand__dot { width: 130px; height: 130px; }
  .card--back .brand__name { font-size: 42px; }

  .person { position: absolute; left: 372px; top: 38px; color: var(--leaf); font-size: 26px; font-weight: 500; }
  .person__role { font-size: 18px; }

  .contact-list { position: absolute; left: 371px; top: 102px; list-style: none; }
  .contact-list__item { display: flex; align-items: flex-start; margin-bottom: 24px; font-size: 23px; line-height: 37px; }
  .contact-list__icon {
    width: 44px; height: 44px; border: 2px solid var(--leaf); border-radius: 50%;
    display: flex; align-items: center; justify-content: center; margin-right: 16px; flex: none;
  }
  .contact-list__icon svg { width: 20px; height: 20px; fill: var(--sky); }
  .contact-list__item--address .contact-list__icon { margin-top: 16px; }

  .tagline {
    position: absolute; left: 0; width: 826px; top: 421px;
    text-align: center; font-size: 19px; font-weight: 500; word-spacing: 1px;
  }
  .tagline span { margin: 0 8px; }

  .back-contacts {
    position: absolute; left: 0; width: 826px; top: 425px;
    display: flex; justify-content: center; gap: 56px; font-size: 19px;
  }
  .back-contacts__item { display: flex; align-items: center; gap: 12px; }
  .back-contacts__item svg { width: 20px; height: 20px; fill: var(--paper); }
</style>
</head>
<body>

<section class="card card--front">
  <svg class="card__waves" viewBox="0 0 826 467" aria-hidden="true">
    <path class="wave--leaf" d="M380 385 C520 358 690 352 826 368 L826 467 L380 467 Z"/>
    <path class="wave--sky" d="M0 410 C150 370 310 362 520 386 C650 399 740 393 826 386 L826 467 L0 467 Z"/>
  </svg>

  <div class="brand">
    <span class="brand__dot"></span>
    <p class="brand__name">Red Fern Coastal<br>Supply</p>
  </div>

  <p class="person">Sam Porter, <span class="person__role">Sales Manager</span></p>

  <ul class="contact-list">
    <li class="contact-list__item">
      <span class="contact-list__icon"><svg viewBox="0 0 24 24"><path d="M2 5h20v2l-10 6L2 7z M2 9l10 6 10-6v10H2z"/></svg></span>
      hello@redferncoastalsupply.example
    </li>
    <li class="contact-list__item">
      <span class="contact-list__icon"><svg viewBox="0 0 24 24"><path d="M6.6 10.8a15 15 0 0 0 6.6 6.6l2.2-2.2a1 1 0 0 1 1-.25 11.4 11.4 0 0 0 3.6.57 1 1 0 0 1 1 1V20a1 1 0 0 1-1 1A17 17 0 0 1 3 4a1 1 0 0 1 1-1h3.5a1 1 0 0 1 1 1c0 1.25.2 2.45.57 3.57a1 1 0 0 1-.25 1z"/></svg></span>
      555-014-2783
    </li>
    <li class="contact-list__item contact-list__item--address">
      <span class="contact-list__icon"><svg viewBox="0 0 24 24"><path d="M12 2a7 7 0 0 0-7 7c0 5.25 7 13 7 13s7-7.75 7-13a7 7 0 0 0-7-7zm0 9.5A2.5 2.5 0 1 1 12 6.5a2.5 2.5 0 0 1 0 5z"/></svg></span>
      <address style="font-style:normal">Harbour Lane Depot,<br>48 Wattle Bay Rd.,<br>Port Alder QLD 4870</address>
    </li>
  </ul>

  <p class="tagline">Aeroponics<span>|</span>Hydroponics<span>|</span>Horticultural<span>|</span>Organics<span>|</span>sustainability space</p>
</section>

<section class="card card--back">
  <svg class="card__waves" viewBox="0 0 826 467" aria-hidden="true">
    <path class="wave--leaf" d="M0 355 C140 348 300 380 430 420 L430 467 L0 467 Z"/>
    <path class="wave--sky" d="M0 398 C200 405 330 418 480 420 C640 422 760 408 826 392 L826 467 L0 467 Z"/>
  </svg>

  <div class="brand">
    <span class="brand__dot"></span>
    <p class="brand__name">Red Fern Coastal<br>Supply</p>
  </div>

  <div class="back-contacts">
    <span class="back-contacts__item">
      <svg viewBox="0 0 24 24"><path d="M3 3h18v18H3z M8 7.5a10 10 0 0 0 8.5 8.5l1.2-1.6-2.4-1.2-1 1a6.5 6.5 0 0 1-4-4l1-1-1.2-2.4z" fill-rule="evenodd"/></svg>
      555-014-2783
    </span>
    <span class="back-contacts__item">
      <svg viewBox="0 0 24 24"><path d="M2 5h20v2l-10 6L2 7z M2 9l10 6 10-6v10H2z"/></svg>
      hello@redferncoastalsupply.example
    </span>
  </div>
</section>

</body>
</html>
```